Design a clean homepage for a travel portal based in the US catering to Asians. The design should be able to be used on other pages, or color scheme menu layout, header and footer should be usable on other pages.

Include the main options for users to click, as an example some could be; 1. Local Tour Company 2. Local Tour Guide 3. Transportation Company 4. Tour Packages

Think like www.brushmarket-example.com who brings designers and clients together we are bringing Tour company, Tour guide, Bus/Transportation company directly to those who need it. This is for a two way portal, not a common one way portal like regular booking sites.

Assume that a person arrives or is planning on arriving at a destination, what are some options that should be on the page, layout of the options: squares, rectangles, stars, scroll slides, whatever makes you feel fun, elegant, fresh, uplifting.

Feelings we want to convey: fun, elegant, fresh, uplifting, interesting, energetic

Update:
When we said this should be a simple design, we meant simple for the end user to understand what was going on. I have attached a screenshot of a website, that it is very easy to understand what its purpose is.

How you decide to set up picture/scenery areas, logo area, menu area, where the options go is all up to you. Would like it to be clean and inviting, we would also like the options to be colors that call the users to action(make them click). This doesn't have to be colors so much as design. If you have further questions feel free to message me.

Attached is our logo in various styles for you to choose from.

Target Market(s)

Travel, package tours, international students, business trips

Industry/Entity Type

Travel Industry

Number of Pages Required

1 page

Colors
ec1f27
ffffff
0255a3
474747
7f7f7f
5c5c5c
aaaaaa

Requirements
Must have
• 1. Local Tour Company 2. Local Tour Guide 3. Transportation Company 4. Tour Packages
Should not have
• Our main goal is not to sell flights or hotel rooms, so this can be an element on the page(or not) but it should not be very central/obvious.

```html
<!DOCTYPE html>
<html lang="en">
<head>
<meta charset="utf-8">
<title>Tripnorth – Travel Portal</title>
<link href="https://fonts.googleapis.com/css2?family=Roboto:wght@300;400;500&family=Roboto+Condensed:wght@300;400&family=Oswald:wght@500;600&display=swap" rel="stylesheet">
<style>
:root{
  --red:#ec1f27;
  --navy:#0255a3;
  --sky:#1b8bd3;
  --sky-dark:#1779bd;
  --ink:#474747;
  --grey:#7f7f7f;
  --grey-mid:#5c5c5c;
  --grey-light:#aaaaaa;
  --white:#ffffff;
  --footer-base:#2f2f2f;
}
*{margin:0;padding:0;box-sizing:border-box}
html,body{width:746px;height:1200px;overflow:hidden}
body{position:relative;background:var(--white);font-family:'Roboto',Arial,sans-serif;font-weight:400;color:var(--ink)}
h1,h2,h3,h4{font-weight:400}

/* header */
.site-header{position:absolute;left:0;top:0;width:746px;height:50px;background:linear-gradient(#2a97dc,var(--sky-dark))}
.brand{position:absolute;left:0;top:0;width:144px;height:50px;background:var(--white);display:flex;align-items:center;justify-content:center;gap:6px}
.brand-dot{width:9px;height:9px;border-radius:50%;background:var(--navy)}
.brand-name{font-size:14px;font-weight:500;color:var(--navy)}
.main-nav{position:absolute;left:144px;top:0;height:50px;display:flex}
.main-nav a{display:block;height:50px;line-height:50px;padding:0 11px;font-family:'Roboto Condensed',Arial,sans-serif;font-weight:300;font-size:8.5px;color:var(--white);text-decoration:none;text-transform:uppercase;margin-right:6px}
.main-nav a.is-active{background:var(--red);padding:0 14px;margin-right:4px}
.header-rule{position:absolute;left:0;top:48px;width:190px;height:2px;background:var(--red)}

/* hero */
.hero{position:absolute;left:0;top:50px;width:746px;height:350px;
  background:
    radial-gradient(ellipse 60% 30% at 30% 78%,rgba(120,130,240,.85),rgba(120,130,240,0) 70%),
    radial-gradient(ellipse 55% 20% at 70% 75%,rgba(200,190,255,.7),rgba(200,190,255,0) 70%),
    radial-gradient(ellipse 40% 25% at 45% 40%,rgba(255,170,70,.8),rgba(255,170,70,0) 70%),
    linear-gradient(180deg,#6d5f6a 0%,#a8714f 25%,#e08d45 42%,#9a5a3c 55%,#3d2a2c 66%,#4b4fa6 84%,#6e78d6 100%)}
.hero-copy{position:absolute;left:421px;top:120px;color:var(--white);text-shadow:0 1px 3px rgba(0,0,0,.45)}
.hero-title{font-family:'Oswald',Arial,sans-serif;font-weight:600;font-size:36px;line-height:42px;letter-spacing:.5px}
.hero-sub{font-family:'Oswald',Arial,sans-serif;font-weight:500;font-size:19px;line-height:24px;margin-left:4px}
.hero-text{font-size:8px;line-height:16px;width:240px;margin-top:6px;font-weight:300}
.hero-arrow{position:absolute;top:210px;width:22px;height:22px;border-radius:50%;background:rgba(40,40,40,.55);display:flex;align-items:center;justify-content:center}

/* services panel */
.services{position:absolute;left:62px;top:364px;width:622px;height:246px;background:var(--white);border-top:2px solid var(--red);box-shadow:0 4px 14px rgba(0,0,0,.18)}
.service{position:absolute;top:18px;width:193px}
.service-photo{width:193px;height:114px;border:1px solid #dcdcdc;padding:4px;background:var(--white)}
.service-photo div{width:100%;height:100%}
.service-title{font-size:11.5px;font-weight:400;color:var(--ink);margin:10px 0 5px 0}
.service-text{font-size:6.8px;line-height:12px;color:var(--grey);font-weight:400}
.more{display:flex;align-items:center;gap:5px;font-size:7px;color:var(--grey-mid);margin-top:8px;padding-left:2px;text-transform:uppercase}

/* welcome */
.welcome-title{position:absolute;left:71px;top:637px;font-size:16px;font-weight:400;color:var(--navy);display:flex;align-items:center;gap:8px}
.welcome-mark{width:30px;height:3px;background:var(--red);border-radius:2px}
.welcome-text{position:absolute;left:71px;top:666px;width:340px;font-size:6.9px;line-height:12.8px;color:var(--grey)}
.welcome-text p{margin-bottom:7px}
.ticks{position:absolute;left:71px;top:760px;list-style:none;font-size:7.5px;color:var(--ink)}
.ticks li{display:flex;align-items:center;gap:9px;height:19px}
.wheel{position:absolute;left:450px;top:620px}

/* news */
.news-head{position:absolute;left:62px;top:869px;width:622px;display:flex;align-items:center;gap:8px;font-size:13px;color:var(--ink)}
.news-head span{flex:1;height:1px;background:#e6e6e6}
.news-item{position:absolute;top:904px;width:290px}
.news-photo{position:absolute;left:0;top:0;width:106px;height:102px;border:1px solid #dcdcdc;padding:3px;background:var(--white)}
.news-photo div{width:100%;height:100%}
.news-date{position:absolute;left:116px;top:0;width:23px;text-align:center}
.news-date b{display:block;background:#555;color:var(--white);font-size:7px;font-weight:400;line-height:10px}
.news-date i{display:block;font-style:normal;font-size:8px;background:#f1f1f1;line-height:13px;color:var(--ink)}
.news-title{position:absolute;left:148px;top:0;width:150px;font-size:10px;font-weight:400;line-height:15px;color:var(--ink)}
.news-text{position:absolute;left:117px;top:37px;width:180px;font-size:6.7px;line-height:12.8px;color:var(--grey)}
.news-more{position:absolute;left:118px;top:94px;font-size:7.5px;font-style:italic;color:var(--ink);display:flex;gap:10px;align-items:center}
.stars{color:#f2a31c;font-size:7px;font-style:normal}
.stars em{color:#c9c9c9;font-style:normal}

/* footer */
.site-footer{position:absolute;left:0;top:1036px;width:746px;height:127px;background:var(--sky);color:var(--white)}
.footer-col{position:absolute;top:21px}
.footer-col h4{font-size:11px;font-weight:300;text-transform:uppercase;margin-bottom:9px}
.footer-small{font-size:7.2px;line-height:12.8px;font-weight:300}
.contact-line{display:flex;align-items:center;gap:8px;margin-top:6px;font-size:8.5px;font-weight:300}
.signup{display:flex;margin-top:9px}
.signup input{width:102px;height:23px;border:1px solid rgba(255,255,255,.45);background:transparent;font-family:inherit;font-size:6.5px;padding-left:8px;color:var(--white)}
.signup input::placeholder{color:rgba(255,255,255,.75)}
.signup button{width:50px;height:23px;border:0;background:#1f2a36;color:var(--white);font-family:inherit;font-size:7.5px}
.social{display:flex;gap:10px;margin-top:4px}
.social span{width:21px;height:21px;background:#eef5fb;border-radius:2px}
.copyright{position:absolute;left:0;top:1163px;width:746px;height:37px;background:var(--footer-base);color:#e5e5e5;font-size:8px;text-align:center;line-height:37px}
</style>
</head>
<body>

<header class="site-header">
  <div class="brand"><span class="brand-dot"></span><span class="brand-name">Tripnorth</span></div>
  <nav class="main-nav">
    <a class="is-active" href="#">Home</a>
    <a href="#">Local Tour Company</a>
    <a href="#">Local Tour Guide</a>
    <a href="#">Transportation</a>
    <a href="#">Hotel/Flight</a>
    <a href="#">Activity</a>
    <a href="#">Contact Us</a>
  </nav>
  <div class="header-rule"></div>
</header>

<section class="hero" role="img" aria-label="Resort terrace with parasols and pools at sunset">
  <div class="hero-copy">
    <div class="hero-title">TRAVEL PORTAL</div>
    <div class="hero-sub">Local Tour Company</div>
    <div class="hero-text">Lorem ipsum dolor sit amet, consectetur adipiscing elit, sed eiusmod tempor incididunt ut labore et dolore</div>
  </div>
  <div class="hero-arrow" style="left:21px"><svg width="8" height="8" viewBox="0 0 8 8"><path d="M5.5 1 2.5 4 5.5 7" fill="none" stroke="#fff" stroke-width="1.3"/></svg></div>
  <div class="hero-arrow" style="left:703px"><svg width="8" height="8" viewBox="0 0 8 8"><path d="M2.5 1 5.5 4 2.5 7" fill="none" stroke="#fff" stroke-width="1.3"/></svg></div>
</section>

<section class="services">
  <article class="service" style="left:10px">
    <div class="service-photo"><div role="img" aria-label="River view of a city landmark tower on a sunny day" style="background:radial-gradient(ellipse 40% 45% at 20% 20%,rgba(255,240,170,.9),rgba(255,240,170,0) 70%),linear-gradient(180deg,#2f6fb5 0%,#7fb2d8 40%,#c9d9c8 55%,#7d8f45 72%,#3e5030 100%)"></div></div>
    <h3 class="service-title">Local Tour Company</h3>
    <p class="service-text">Lorem ipsum dolor sit amet, consectetur adipiscing elit, sed do eiusmod tempor incididunt ut labore et dolore magna aliqua. Ut enim ad minim</p>
    <div class="more">Click here <svg width="7" height="7" viewBox="0 0 8 8"><circle cx="4" cy="4" r="4" fill="#474747"/><path d="M3.2 2.3 4.9 4 3.2 5.7" fill="none" stroke="#fff" stroke-width="1.1"/></svg></div>
  </article>
  <article class="service" style="left:215px">
    <div class="service-photo"><div role="img" aria-label="Two young travellers with a guidebook in an old town street" style="background:radial-gradient(ellipse 30% 50% at 85% 75%,rgba(230,80,150,.85),rgba(230,80,150,0) 70%),radial-gradient(ellipse 35% 50% at 50% 70%,rgba(110,120,80,.8),rgba(110,120,80,0) 70%),linear-gradient(180deg,#c8c3b8 0%,#b2a894 50%,#8c8472 100%)"></div></div>
    <h3 class="service-title">Local Tour Guide</h3>
    <p class="service-text">Lorem ipsum dolor sit amet, consectetur adipiscing elit, sed do eiusmod tempor incididunt ut labore et dolore magna aliqua. Ut enim ad minim</p>
    <div class="more">Click here <svg width="7" height="7" viewBox="0 0 8 8"><circle cx="4" cy="4" r="4" fill="#474747"/><path d="M3.2 2.3 4.9 4 3.2 5.7" fill="none" stroke="#fff" stroke-width="1.1"/></svg></div>
  </article>
  <article class="service" style="left:420px">
    <div class="service-photo"><div role="img" aria-label="Tour group on a scenic coach trip through the countryside" style="background:radial-gradient(ellipse 45% 35% at 70% 25%,rgba(255,250,220,.9),rgba(255,250,220,0) 70%),linear-gradient(180deg,#5aa0d8 0%,#a9cfe8 42%,#d7c79a 58%,#8a9a4c 75%,#4d5d32 100%)"></div></div>
    <h3 class="service-title">Tour Packages</h3>
    <p class="service-text">Lorem ipsum dolor sit amet, consectetur adipiscing elit, sed do eiusmod tempor incididunt ut labore et dolore magna aliqua. Ut enim ad minim</p>
    <div class="more">Click here <svg width="7" height="7" viewBox="0 0 8 8"><circle cx="4" cy="4" r="4" fill="#474747"/><path d="M3.2 2.3 4.9 4 3.2 5.7" fill="none" stroke="#fff" stroke-width="1.1"/></svg></div>
  </article>
</section>

<h2 class="welcome-title">WELCOME TO TRIPNORTH <span class="welcome-mark"></span></h2>
<div class="welcome-text">
  <p>Lorem ipsum dolor sit amet, consectetur adipiscing elit, sed do eiusmod tempor incididunt ut labore et dolore magna aliqua. Ut enim ad minim veniam, quis nostrud exercitation ullamco laboris nisi ut aliquip ex ea commodo consequat. Duis aute irure dolor in reprehenderit in voluptate velit esse cillum dolore eu fugiat nulla pariatur. Excepteur sint occaecat cupidatat non proident, sunt in culpa qui officia</p>
  <p>Lorem ipsum dolor sit amet, consectetur adipiscing elit, sed do eiusmod tempor incididunt ut labore et dolore magna aliqua. Ut enim ad minim veniam, quis nostrud exercitation</p>
</div>
<ul class="ticks">
  <li><svg width="8" height="7" viewBox="0 0 8 7"><path d="M1 3.6 3 5.6 7 1.2" fill="none" stroke="#0255a3" stroke-width="1.6"/></svg>Nemo enim ipsam voluptatem quia</li>
  <li><svg width="8" height="7" viewBox="0 0 8 7"><path d="M1 3.6 3 5.6 7 1.2" fill="none" stroke="#0255a3" stroke-width="1.6"/></svg>Sed ut perspiciatis unde omnis iste natus</li>
  <li><svg width="8" height="7" viewBox="0 0 8 7"><path d="M1 3.6 3 5.6 7 1.2" fill="none" stroke="#0255a3" stroke-width="1.6"/></svg>Neque porro quisquam est, qui dolorem ipsum</li>
</ul>

<svg class="wheel" width="220" height="220" viewBox="-110 -110 220 220" font-family="Roboto, Arial, sans-serif" font-size="7" fill="#fff" text-anchor="middle">
  <path d="M0 0 L-70.1 -83.5 A109 109 0 0 1 0 -109 Z" fill="#2aa3dd"/>
  <path d="M0 0 L0 -109 A109 109 0 0 1 77.1 -77.1 Z" fill="#1bb39a"/>
  <path d="M0 0 L77.1 -77.1 A109 109 0 0 1 107.3 18.9 Z" fill="#8cc63f"/>
  <path d="M0 0 L107.3 18.9 A109 109 0 0 1 54.5 94.4 Z" fill="#5b5b5b"/>
  <path d="M0 0 L54.5 94.4 A109 109 0 0 1 -18.9 107.3 Z" fill="#f3d94a"/>
  <path d="M0 0 L-18.9 107.3 A109 109 0 0 1 -70.1 -83.5 Z" fill="#e3232b"/>
  <circle r="48" fill="#fff"/>
  <circle cx="-25" cy="0" r="3.5" fill="#0255a3"/>
  <text x="4" y="4" font-size="12" font-weight="500" fill="#0255a3">Tripnorth</text>
  <rect x="-30" y="-84" width="11" height="14" fill="#fff"/>
  <text x="-24" y="-60">HOTEL</text>
  <path d="M32 -84 l4 6 -8 3 v2 l8 -1 3 6 2 -1 -1 -6 7 -2 -1 -2 -7 1 z" fill="#fff"/>
  <text x="32" y="-61">FLIGHT</text>
  <path d="M72 -32 l4 5 -7 3 v2 l7 -1 2 5 2 -1 -1 -5 6 -2 -1 -2 -6 1 z" fill="#fff"/>
  <text x="70" y="-9">FOOD</text>
  <circle cx="62" cy="25" r="4" fill="none" stroke="#fff" stroke-width="1.5"/>
  <text x="74" y="44">TOUR GUIDE</text>
  <circle cx="30" cy="69" r="7" fill="none" stroke="#fff" stroke-width="1.3"/>
  <path d="M30 65 v4 h3" stroke="#fff" stroke-width="1.2" fill="none"/>
  <text x="28" y="91" transform="rotate(-25 28 91)">TRANSPORTATION</text>
  <circle cx="-77" cy="7" r="8" fill="none" stroke="#fff" stroke-width="1.4"/>
  <path d="M-85 7 h16 M-77 -1 v16" stroke="#fff" stroke-width="1"/>
  <text x="-76" y="33">LOCAL TOUR</text>
  <text x="-76" y="45">COMPANY</text>
</svg>

<div class="news-head">LATEST NEWS <span></span></div>

<article class="news-item" style="left:62px">
  <div class="news-photo"><div role="img" aria-label="Businesswoman reading a tablet in an airport lounge" style="background:radial-gradient(ellipse 35% 55% at 50% 70%,rgba(40,40,45,.9),rgba(40,40,45,0) 75%),linear-gradient(180deg,#d5dde3 0%,#9aa6ae 55%,#5b6168 100%)"></div></div>
  <div class="news-date"><b>03</b><i>Sep</i></div>
  <h3 class="news-title">Nemo enim ipsam volup quia voluptas sit</h3>
  <p class="news-text">Lorem ipsum dolor sit amet, consectetur adipiscing elit, sed do eiusmod tempor incididunt ut labore et dolore magna aliqua. Ut enim ad minim veniam, quis nostrud exercitation ullamco</p>
  <div class="news-more">READ MORE <span class="stars">★★★<em>☆☆</em></span></div>
</article>

<article class="news-item" style="left:396px">
  <div class="news-photo"><div role="img" aria-label="Hiker with backpack on a hilltop at sunrise" style="background:radial-gradient(ellipse 45% 40% at 50% 45%,rgba(255,245,190,.95),rgba(255,245,190,0) 70%),linear-gradient(180deg,#d98a2c 0%,#f2c258 45%,#a9692a 72%,#4a3424 100%)"></div></div>
  <div class="news-date"><b>03</b><i>Sep</i></div>
  <h3 class="news-title">Nemo enim ipsam volup quia voluptas sit</h3>
  <p class="news-text">Lorem ipsum dolor sit amet, consectetur adipiscing elit, sed do eiusmod tempor incididunt ut labore et dolore magna aliqua. Ut enim ad minim veniam, quis nostrud exercitation ullamco</p>
  <div class="news-more">READ MORE <span class="stars">★★★<em>☆☆</em></span></div>
</article>

<footer class="site-footer">
  <div class="footer-col" style="left:60px">
    <h4>Contact Us</h4>
    <p class="footer-small">Tripnorth 2210 Maple Rd.<br>&nbsp;Cedar Falls, MI 48000 USA</p>
    <div class="contact-line" style="margin-top:8px"><svg width="10" height="10" viewBox="0 0 10 10"><path d="M2 1 4 3 3 4.3 5.7 7 7 6 9 8 7.6 9.4C4 9 1 6 .6 2.4Z" fill="none" stroke="#fff" stroke-width=".9"/></svg>(+901) 555-0142</div>
    <div class="contact-line" style="font-size:7.5px"><svg width="10" height="8" viewBox="0 0 10 8"><rect x=".5" y=".5" width="9" height="7" fill="none" stroke="#fff" stroke-width=".9"/><path d="M.5 .5 5 4.5 9.5 .5" fill="none" stroke="#fff" stroke-width=".9"/></svg>hello@tripnorth.example</div>
  </div>
  <div class="footer-col" style="left:227px">
    <h4>Latest Tweet`s</h4>
    <div style="display:flex;gap:11px">
      <span style="width:11px;height:11px;background:#fff;border-radius:2px;flex:none;margin-top:1px"></span>
      <p class="footer-small" style="width:122px;font-size:6.8px">Phasellus porta. Fusce susct varius mi. Cum sociis natoque penabus et magnis dis parturient montes, nas- cetur ridiculus mus. See more here http://t.co/example01</p>
    </div>
  </div>
  <div class="footer-col" style="left:414px">
    <h4>Newsletter</h4>
    <p class="footer-small" style="width:160px;font-size:6.8px">Excepteur sint occaecat cupidatat non proident, sunt in culpa qui officia deserunt mollit anim</p>
    <form class="signup"><input type="text" placeholder="Enter your email address"><button type="button">SIGN UP</button></form>
  </div>
  <div class="footer-col" style="left:600px">
    <h4>Social Media</h4>
    <div class="social"><span></span><span></span><span></span></div>
  </div>
</footer>
<div class="copyright">2015 &nbsp;All Rights Reserved. Tripnorth</div>

</body>
</html>
```